4" x 6" Coffee Label for a Fundraising Project

You will be designing a full-color label for a coffee product.
This particular design is for a school band fundraising program, and should align with the school existing webiste in terms of 'look and feel.'
You may choose any one of the following coffee blends to build your design around: breakfast blend, sumatra, hazelnut, house blend decaf, mocha, pumpkin spice, candy cane or cinnabun. (Yes, we will need multiple labels in the near future.) Your design for a label should be expandable to other coffee varieties and leverage some brand elements across different labels to reflect brand consistency.
What is the brand? It is a k-12 school, the fundraisor is for the school's music / band program. The primary colors are red, white and black; however you should incorporate other colors that represent the coffee blend (from the above list).
Who is the target market? Coffee drinkers! (So your design should reflect the positive qualities of coffee) They are also parents, friends and alumni of the school.
What is the brand's feel? Your design should bring to mind the following when drinkers view the label on the package: high quality, a luxury drink, aligned with christian values, perhaps a sense of community, and the school's band and/or performing arts. (Please note that this design is specific to the band program.)
Can I create a name for any of the above blends that has band connetations? Yes! Actually, ideating band-related names is encouraged. If your design uses Lantern Ballad or Meadow Minuet for the breakfast blend, or Cobalt Caper or Harbor Overture for the mocha blend - AWESOME! So get creative in renaming the blends appropraitely and incorporating this into your overall design. Even better if your naming convention and design could be leveraged across several different coffee blends.
If you incorporate photo imagery in your design, note that we will need to procure similar images we own or can license. Thus, photo imagery should be FPO and representative of they type of imagery for the design.
Specifications for the design are:
1. 4" wide x 6" tall portrait layout
2. 1600 x 2400 pixes
3. CYML for printing
4. Note that the bottom third must be left completely clean - no design elements or text - for NBQ required labeling.
5. Design must be completed in Adobe Photoshop or Illustrator.
6. All incorporated fonts must be available for use without licensing.

```html
<!DOCTYPE html>
<html lang="en">
<head>
<meta charset="utf-8">
<title>Bramwell Coffee – Breakfast Blend Label</title>
<link rel="stylesheet" href="https://fonts.googleapis.com/css2?family=Lobster&family=Oswald:wght@400;500&display=swap">
<style>
  :root {
    --page: #e4e4e4;
    --label: #ffffff;
    --red: #d40000;
    --red-deep: #8f0000;
    --charcoal: #333132;
    --cream: #f1d9b5;
    --ink: #111111;
  }
  * { margin: 0; padding: 0; box-sizing: border-box; }
  html, body {
    width: 1200px;
    height: 750px;
    overflow: hidden;
    background: var(--page);
  }
  .stage {
    position: relative;
    width: 1200px;
    height: 750px;
  }
  .label {
    position: absolute;
    left: 370px;
    top: 30px;
    width: 460px;
    height: 690px;
    background: var(--label);
    box-shadow: 0 14px 22px rgba(0, 0, 0, 0.18);
    overflow: hidden;
  }
  .label__artwork {
    position: absolute;
    left: 0;
    top: 0;
    width: 460px;
    height: 460px;
    display: block;
  }
  .label__clear-zone {
    position: absolute;
    left: 0;
    top: 460px;
    width: 460px;
    height: 230px;
    background: var(--label);
  }
  .brand-name {
    font-family: "Oswald", sans-serif;
    font-weight: 500;
    font-size: 52px;
    fill: var(--red);
    letter-spacing: 1px;
  }
  .blend-pair {
    font-family: "Oswald", sans-serif;
    font-weight: 400;
    font-size: 12.5px;
    fill: var(--cream);
    letter-spacing: 0.3px;
  }
  .blend-title {
    font-family: "Lobster", cursive;
    font-size: 29px;
    fill: var(--cream);
  }
</style>
</head>
<body>
<main class="stage">
  <article class="label">
    <svg class="label__artwork" viewBox="0 0 460 460" xmlns="http://www.w3.org/2000/svg">
      <defs>
        <radialGradient id="burst-tone" cx="50%" cy="48%" r="70%">
          <stop offset="0%" stop-color="var(--red)"/>
          <stop offset="70%" stop-color="#b30000"/>
          <stop offset="100%" stop-color="var(--red-deep)"/>
        </radialGradient>
      </defs>

      <rect class="sunburst" x="0" y="0" width="460" height="460" fill="url(#burst-tone)"
            role="img" aria-label="Red and black sunburst rays with distressed speckle texture"/>

      <rect class="cross-band" x="0" y="185" width="460" height="106" fill="var(--charcoal)"/>

      <path class="center-panel" d="M86 0 H374 V288 A144 144 0 0 1 86 288 Z" fill="var(--charcoal)"/>

      <g class="badge">
        <polygon points="230,11 352,38 352,158 230,185 108,158 108,38"
                 fill="none" stroke="var(--red)" stroke-width="1.6" stroke-linejoin="round"/>
        <rect x="131" y="39" width="199" height="77" rx="8"
              fill="none" stroke="var(--cream)" stroke-width="1.6"/>
        <text class="brand-name" x="230" y="97" text-anchor="middle">Bramwell</text>
        <text class="blend-pair" x="230" y="141" text-anchor="middle">LANTERN BALLAD &amp; MEADOW MINUET</text>
      </g>

      <g class="ribbon">
        <polygon points="67,263 81,263 81,275" fill="var(--red-deep)"/>
        <polygon points="394,263 380,263 380,275" fill="var(--red-deep)"/>
        <rect x="67" y="215" width="327" height="48" fill="var(--red)"/>
        <text class="blend-title" x="230" y="250" text-anchor="middle">breakfast blend</text>
      </g>

      <circle class="roast-emblem" cx="230" cy="358" r="58" fill="var(--charcoal)"
              stroke="var(--cream)" stroke-width="2"
              role="img" aria-label="Roasted beans emblem with steaming coffee cup line drawing"/>
    </svg>
    <div class="label__clear-zone"></div>
  </article>
</main>
</body>
</html>
```